Wedding Planning and Event Planners website

I am driven by perfection of my occupation and i look forward to having an attractive and contemporary website for an event and wedding planning group. We are located in the United States and Canada and we offer our services only in these two countries. My website is for people who are planning events such Church programs, weddings, musical concerts, Picnic, etc. My website should have imaginary of events such as weddings, musical concerts and picnic, etc.. I don't have any reference website because i want all designers to be creative and unique. I prefer blue,red,green,yellow colors.

Industry/Entity Type

Wedding

Coding

Coded - Design and coding required

```html
<!DOCTYPE html>
<html lang="en">
<head>
<meta charset="utf-8">
<title>Bloomfield Events</title>
<link rel="stylesheet" href="https://fonts.googleapis.com/css2?family=Noto+Sans:wght@400;700&family=Open+Sans:wght@300;400&display=swap">
<style>
:root{
  --ink-dark:#07050f;
  --header-bg:#0b0914;
  --footer-bg:#1b1a1f;
  --white:#ffffff;
  --text-soft:#f1eef8;
  --btn-text:#d2232f;
  --caption-bg:rgba(74,120,52,.82);
  --blue-1:#1f6f9e;
  --blue-2:#4fa7cf;
  --purple-1:#2a0c55;
  --purple-2:#7a1d9a;
  --magenta:#a0208f;
  --green-1:#1f7a4d;
  --green-2:#5daa6e;
  --red-1:#d84b55;
  --red-2:#ec7577;
  --footer-text:#8d8a93;
}
*{margin:0;padding:0;box-sizing:border-box}
html,body{width:1200px;height:2446px;overflow:hidden}
body{font-family:"Noto Sans",Verdana,sans-serif;color:var(--white);background:var(--ink-dark)}

.site-header{height:76px;background:var(--header-bg);display:flex;align-items:center;justify-content:space-between;padding:0 36px 0 76px}
.brand{display:flex;align-items:center;gap:10px;font-size:15px;font-weight:700;color:#f4d13a;letter-spacing:.5px}
.brand-mark{width:14px;height:14px;border-radius:50%;background:#f4d13a}
.main-nav{display:flex;gap:24px;list-style:none;font-size:14px;font-weight:700}

.hero{position:relative;height:402px;background:linear-gradient(100deg,#3a2a26 0%,#8a6f63 22%,#b9a79c 40%,#e9e4ea 52%,#7d3f8a 70%,#b46aa7 85%,#e3b59b 100%)}
.hero-caption{position:absolute;left:596px;top:312px;width:587px;height:34px;background:var(--caption-bg);font-family:"Open Sans",sans-serif;font-weight:300;font-size:16.5px;line-height:34px;padding-left:9px;color:var(--white);white-space:nowrap;overflow:hidden}
.hero-dots{position:absolute;left:583px;top:369px;display:flex;gap:6px}
.hero-dots span{width:14px;height:14px;border-radius:50%;border:2px solid var(--white)}
.hero-dots span.active{background:var(--white)}

.welcome{height:261px;text-align:center;padding-top:68px;background:radial-gradient(ellipse 520px 260px at 62% 20%,var(--magenta) 0%,rgba(160,32,143,0) 100%),radial-gradient(ellipse 420px 260px at 22% 40%,#2a2aa8 0%,rgba(42,42,168,0) 100%),var(--ink-dark)}
.welcome h1{font-weight:400;font-size:29px;letter-spacing:.5px;margin-bottom:8px}
.welcome .lead{font-size:12.5px;margin-bottom:4px}
.welcome p{font-size:12.5px;line-height:21px;width:680px;margin:0 auto;color:var(--text-soft)}

.event{display:flex;align-items:center;padding-left:120px}
.event-body{width:611px}
.event h2{font-weight:400;font-size:27px;margin-bottom:4px}
.event p{font-size:12.5px;line-height:20.5px;color:var(--text-soft)}
.read-more{display:inline-block;margin-top:26px;width:106px;height:33px;line-height:33px;padding-left:10px;background:var(--white);color:var(--btn-text);border-radius:3px;font-size:13px;text-decoration:none}
.event-photo{width:285px;border:1px solid rgba(255,255,255,.6)}
.event--text-first .event-photo{margin-left:64px}
.event--photo-first .event-photo{margin-right:52px}

.event--wedding{height:334px;background:radial-gradient(circle 70px at 88% 72%,rgba(255,255,255,.3),rgba(255,255,255,0)),linear-gradient(150deg,var(--blue-1) 0%,var(--blue-2) 55%,#3e8fc0 100%)}
.event--music{height:328px;background:radial-gradient(ellipse 520px 300px at 62% 40%,var(--magenta),rgba(160,32,143,0)),linear-gradient(90deg,var(--ink-dark) 0%,var(--purple-1) 35%,var(--purple-2) 70%,var(--ink-dark) 100%)}
.event--church{height:334px;background:radial-gradient(circle 70px at 88% 70%,rgba(255,255,255,.25),rgba(255,255,255,0)),linear-gradient(150deg,var(--green-1) 0%,var(--green-2) 55%,#3b8d5a 100%)}
.event--picnic{height:329px;background:radial-gradient(ellipse 520px 300px at 62% 40%,var(--magenta),rgba(160,32,143,0)),linear-gradient(90deg,var(--ink-dark) 0%,#1e1a7a 35%,var(--purple-2) 70%,var(--ink-dark) 100%)}
.event--other{height:333px;background:radial-gradient(circle 260px at 30% 80%,rgba(255,160,160,.35),rgba(255,160,160,0)),linear-gradient(150deg,var(--red-1) 0%,var(--red-2) 55%,#d84a55 100%)}

.photo-wedding{height:189px;background:linear-gradient(120deg,#2c5f8f,#cfd6e2 55%,#b32a35 75%,#88b1d3)}
.photo-music{height:171px;background:linear-gradient(120deg,#12153a,#5a2a8a 45%,#d83a5a 70%,#1a1f5a)}
.photo-church{height:188px;background:linear-gradient(180deg,#5b4a3a,#a98f6a 45%,#b83a3a 75%,#3a2a22)}
.photo-picnic{height:170px;background:linear-gradient(180deg,#6fb4e6 0%,#cde7f5 45%,#e9dcb8 70%,#d8c39a 100%)}
.photo-other{height:187px;background:linear-gradient(120deg,#b287d0,#f1c7d6 45%,#e86a8a 70%,#f4d27a)}

.site-footer{height:49px;background:var(--footer-bg);display:flex;align-items:center;justify-content:space-between;padding:0 48px 0 64px;font-size:12.5px;color:var(--footer-text)}
.social{display:flex;gap:22px}
.social span{width:18px;height:18px;border-radius:50%;background:var(--footer-text)}
</style>
</head>
<body>
<header class="site-header">
  <div class="brand"><span class="brand-mark"></span>BLOOMFIELD EVENTS</div>
  <ul class="main-nav">
    <li>Home</li>
    <li>Wedding Events</li>
    <li>Music concert</li>
    <li>Church and religious events</li>
    <li>Picnic and holidays trip</li>
    <li>Other Events</li>
  </ul>
</header>

<section class="hero" role="img" aria-label="Photo of a bride and groom kissing at a church door while guests applaud">
  <div class="hero-caption">Find Wedding Planner &amp; Consultantfor Your Special &amp; Unique Wedding</div>
  <div class="hero-dots"><span class="active"></span><span></span></div>
</section>

<section class="welcome">
  <h1>WELCOME TO BLOOMFIELD EVENTS!</h1>
  <div class="lead">Fusce interdum metus et turpis ornare sed</div>
  <p>Neque porro quisquam est, qui dolorem ipsum quia dolor sit amet, consectetur, adipisci velit, sed quia non numquam eius modi tempora incidunt ut labore et dolore magnam aliquam quaerat voluptatem. Ut enim ad minima veniam, quis nostrum.</p>
</section>

<section class="event event--wedding event--text-first">
  <div class="event-body">
    <h2>Wedding Events</h2>
    <p>Neque porro quisquam est, qui dolorem ipsum quia dolor sit amet, consectetur, adipisci velit, sed quia non numquam eius modi tempora incidunt ut labore et dolore magnam aliquam quaerat voluptatem. Ut enim ad minima veniam, quis nostrum.Neque porro quisquam est, qui dolorem ipsum quia dolor sit amet, consectetur, adipisci velit.</p>
    <a class="read-more" href="#">Read more..</a>
  </div>
  <div class="event-photo photo-wedding" role="img" aria-label="Photo of a bride holding red roses beside the groom"></div>
</section>

<section class="event event--music event--photo-first">
  <div class="event-photo photo-music" role="img" aria-label="Photo of a DJ performing under colourful stage lights"></div>
  <div class="event-body">
    <h2>Music Concert</h2>
    <p>Neque porro quisquam est, qui dolorem ipsum quia dolor sit amet, consectetur, adipisci velit, sed quia non numquam eius modi tempora incidunt ut labore et dolore magnam aliquam quaerat voluptatem. Ut enim ad minima veniam, quis nostrum.Neque porro quisquam est, qui dolorem ipsum quia dolor sit amet, consectetur, adipisci velit.</p>
    <a class="read-more" href="#">Read more..</a>
  </div>
</section>

<section class="event event--church event--text-first">
  <div class="event-body">
    <h2>Church Programes</h2>
    <p>Neque porro quisquam est, qui dolorem ipsum quia dolor sit amet, consectetur, adipisci velit, sed quia non numquam eius modi tempora incidunt ut labore et dolore magnam aliquam quaerat voluptatem. Ut enim ad minima veniam, quis nostrum.Neque porro quisquam est, qui dolorem ipsum quia dolor sit amet, consectetur, adipisci velit.</p>
    <a class="read-more" href="#">Read more..</a>
  </div>
  <div class="event-photo photo-church" role="img" aria-label="Photo of a children's choir on a church stage"></div>
</section>

<section class="event event--picnic event--photo-first">
  <div class="event-photo photo-picnic" role="img" aria-label="Photo of a family running along a tropical beach"></div>
  <div class="event-body">
    <h2>Picnic and holidays trip</h2>
    <p>Neque porro quisquam est, qui dolorem ipsum quia dolor sit amet, consectetur, adipisci velit, sed quia non numquam eius modi tempora incidunt ut labore et dolore magnam aliquam quaerat voluptatem. Ut enim ad minima veniam, quis nostrum.Neque porro quisquam est, qui dolorem ipsum quia dolor sit amet, consectetur, adipisci velit.</p>
    <a class="read-more" href="#">Read more..</a>
  </div>
</section>

<section class="event event--other event--text-first">
  <div class="event-body">
    <h2>Other Events</h2>
    <p>Neque porro quisquam est, qui dolorem ipsum quia dolor sit amet, consectetur, adipisci velit, sed quia non numquam eius modi tempora incidunt ut labore et dolore magnam aliquam quaerat voluptatem. Ut enim ad minima veniam, quis nostrum.Neque porro quisquam est, qui dolorem ipsum quia dolor sit amet, consectetur, adipisci velit.</p>
    <a class="read-more" href="#">Read more..</a>
  </div>
  <div class="event-photo photo-other" role="img" aria-label="Photo of a mother and child at a birthday party with balloons"></div>
</section>

<footer class="site-footer">
  <div>Copyright © 2016 Bloomfield Events</div>
  <div class="social" aria-label="Social links"><span></span><span></span><span></span><span></span></div>
</footer>
</body>
</html>
```